Oven Cleaning Business owner needs business card design

Hi there,
Would like for a business card to be designed for myself, the owner of a professional oven cleaning business on the Sunshine Coast.
Would like it to look sleek, and modern-ish. Bit creative is encouraged too.
Include following:
Name/title: Corin ter Haghe, Owner
Phone number: 1300 482 916
Email: info@hearthshinecrew.com.au
Website: www.hearthshinecrew.com.au

```html
<!DOCTYPE html>
<html lang="en">
<head>
<meta charset="utf-8">
<title>Hearthshine Crew – Business Card</title>
<link rel="stylesheet" href="https://fonts.googleapis.com/css2?family=Lexend:wght@300;400;600&display=swap">
<style>
  :root {
    --ink: #0a0b0b;
    --teal: #52c4cc;
    --paper: #ffffff;
    --backdrop: #d6d6d6;
    --text: #111111;
  }
  * { margin: 0; padding: 0; box-sizing: border-box; }
  html, body { width: 1200px; height: 1200px; overflow: hidden; }
  body {
    background: var(--backdrop);
    font-family: "Lexend", Arial, sans-serif;
    position: relative;
  }
  .card {
    position: absolute;
    left: 268px;
    width: 692px;
    height: 395px;
    overflow: hidden;
  }
  .card--front { top: 119px; background: var(--paper); }
  .card--back { top: 657px; background: var(--ink); }

  .front-art { position: absolute; inset: 0; width: 100%; height: 100%; }

  .front-brand {
    position: absolute;
    left: 38px; top: 112px;
    width: 244px;
    text-align: center;
    color: var(--ink);
    font-weight: 600;
    font-size: 19px;
    line-height: 1.15;
    letter-spacing: 0.04em;
    text-transform: uppercase;
  }
  .front-brand .brand-dot {
    display: block;
    width: 34px; height: 34px;
    margin: 0 auto 12px;
    border-radius: 50%;
    background: var(--teal);
  }

  .contact {
    position: absolute;
    left: 346px; top: 0;
    width: 300px;
  }
  .contact__name {
    position: absolute; top: 68px; left: 0;
    white-space: nowrap;
    font-weight: 600;
    font-size: 26px;
    color: var(--text);
    letter-spacing: 0.01em;
  }
  .contact__name .surname { color: var(--teal); }
  .contact__title {
    position: absolute; top: 99px; left: 0;
    font-weight: 300;
    font-size: 20px;
    color: var(--teal);
  }
  .dot-rule {
    position: absolute; left: 4px;
    width: 292px; height: 4px;
    background-image: radial-gradient(circle, var(--teal) 1.6px, transparent 1.9px);
    background-size: 11.2px 4px;
  }
  .dot-rule--top { top: 136px; }
  .dot-rule--bottom { top: 273px; }
  .contact__row {
    position: absolute; left: 0;
    display: flex; align-items: center;
    font-size: 15.5px;
    color: var(--text);
    white-space: nowrap;
  }
  .contact__row svg { width: 16px; height: 16px; margin-right: 24px; flex: none; }
  .contact__row--phone { top: 180px; }
  .contact__row--email { top: 214px; }
  .contact__row--web { top: 296px; }

  .back-mark {
    position: absolute;
    left: 164px; top: 114px;
    width: 112px; height: 112px;
    border-radius: 50%;
    background: var(--teal);
  }
  .back-brand {
    position: absolute;
    left: 312px; top: 130px;
    color: var(--teal);
    font-weight: 600;
    text-transform: uppercase;
    line-height: 1;
  }
  .back-brand__main { display: block; font-size: 33px; letter-spacing: 0.02em; }
  .back-brand__sub { display: block; font-size: 19px; letter-spacing: 0.62em; margin-top: 12px; }
  .back-web {
    position: absolute;
    left: 312px; top: 234px;
    display: flex; align-items: center;
    color: var(--teal);
    font-size: 17px;
    white-space: nowrap;
  }
  .back-web svg { width: 15px; height: 15px; margin-right: 19px; }
  .back-rule {
    position: absolute; left: 0; right: 0;
    top: 333px; height: 7px;
    background: var(--paper);
  }
  .back-band {
    position: absolute; left: 0; right: 0;
    top: 340px; bottom: 0;
    background: var(--teal);
  }
  .social {
    position: absolute; right: 18px; top: 361px;
    display: flex; gap: 12px;
  }
  .social span {
    width: 22px; height: 22px;
    border-radius: 50%;
    background: var(--paper);
  }
</style>
</head>
<body>

<section class="card card--front" aria-label="Business card front">
  <svg class="front-art" viewBox="0 0 1107 631" preserveAspectRatio="none" aria-hidden="true">
    <path d="M0 0 H214 Q188 100 178 160 L178 500 L290 530 Q325 590 345 631 H0 Z" fill="var(--ink)"/>
    <path d="M232 0 Q210 80 202 130" fill="none" stroke="var(--teal)" stroke-width="38"/>
    <path d="M290 515 Q350 590 395 640" fill="none" stroke="var(--teal)" stroke-width="52"/>
    <circle cx="256" cy="314" r="216" fill="var(--teal)"/>
    <circle cx="256" cy="314" r="193" fill="var(--paper)"/>
  </svg>

  <div class="front-brand">
    <span class="brand-dot"></span>
    Hearthshine<br>Crew
  </div>

  <div class="contact">
    <h1 class="contact__name">Corin ter <span class="surname">Haghe</span></h1>
    <p class="contact__title">Owner</p>
    <div class="dot-rule dot-rule--top"></div>

    <p class="contact__row contact__row--phone">
      <svg viewBox="0 0 24 24" aria-hidden="true"><path fill="var(--text)" d="M6.6 2.5l3 4.2-2 2.1c1 2.7 3 4.9 5.6 6.1l2-2 4.3 2.8-1.4 3.6c-.4.9-1.3 1.3-2.2 1.1C8.9 19 4.5 13.6 3.3 6.6c-.2-1 .3-1.9 1.2-2.3z"/></svg>
      1300 482 916
    </p>
    <p class="contact__row contact__row--email">
      <svg viewBox="0 0 24 24" aria-hidden="true"><rect x="2" y="5" width="20" height="14" fill="var(--text)"/><path d="M2.5 5.5 L12 13 L21.5 5.5" fill="none" stroke="var(--paper)" stroke-width="1.6"/></svg>
      info@hearthshinecrew.com.au
    </p>

    <div class="dot-rule dot-rule--bottom"></div>

    <p class="contact__row contact__row--web">
      <svg viewBox="0 0 24 24" aria-hidden="true"><g fill="none" stroke="#555" stroke-width="1.6"><circle cx="12" cy="12" r="9.5"/><ellipse cx="12" cy="12" rx="4.2" ry="9.5"/><path d="M2.5 12h19M4 7h16M4 17h16"/></g></svg>
      www.hearthshinecrew.com.au
    </p>
  </div>
</section>

<section class="card card--back" aria-label="Business card back">
  <span class="back-mark"></span>
  <p class="back-brand">
    <span class="back-brand__main">Hearthshine</span>
    <span class="back-brand__sub">Crew</span>
  </p>
  <p class="back-web">
    <svg viewBox="0 0 24 24" aria-hidden="true"><g fill="none" stroke="var(--teal)" stroke-width="1.8"><circle cx="12" cy="12" r="9.5"/><ellipse cx="12" cy="12" rx="4.2" ry="9.5"/><path d="M2.5 12h19M4 7h16M4 17h16"/></g></svg>
    www.hearthshinecrew.com.au
  </p>
  <div class="back-rule"></div>
  <div class="back-band"></div>
  <div class="social" aria-label="Social media links">
    <span></span><span></span><span></span>
  </div>
</section>

</body>
</html>
```